Willowbend Pharmacy Business Cards

I need a business card design and or template. Needs to convey a softer feel along with health and wellness. Please see attached logo and color scheme.

Industry/Entity Type

Pharmacy

Colors

Designer to choose colors to be used in the design.

Requirements
Must have
• I've added a second NEW colored logo I think I am going to go with the blue green logo.
• Needs to have the colors and feel of the logo attached.
• Dorian Kessel
• Pharmacy Manager
• willowbendpharmacy.example

```html
<!DOCTYPE html>
<html lang="en">
<head>
<meta charset="utf-8">
<title>Willowbend Pharmacy Business Cards</title>
<link rel="stylesheet" href="https://fonts.googleapis.com/css2?family=Josefin+Sans:wght@600&family=Open+Sans:wght@400;700&display=swap">
<style>
  :root {
    --page: #e9e7e3;
    --card: #232323;
    --white: #ffffff;
    --green: #9cc63b;
    --blue: #35a6dd;
  }
  * { margin: 0; padding: 0; box-sizing: border-box; }
  html, body { width: 1200px; height: 1000px; overflow: hidden; }
  body { background: var(--page); position: relative; font-family: "Open Sans", sans-serif; }

  .card {
    position: absolute; left: 268px; width: 664px; height: 395px;
    background: var(--card); border-radius: 24px; overflow: hidden;
    box-shadow: 0 6px 14px rgba(0,0,0,.25);
  }
  .card--front { top: 75px; }
  .card--back { top: 535px; }

  .brand { position: absolute; display: flex; flex-direction: column; align-items: flex-end; }
  .brand__row { display: flex; align-items: center; gap: 14px; }
  .brand__dot { width: 26px; height: 26px; border-radius: 50%; background: var(--green); flex: none; }
  .brand__name {
    font-family: "Josefin Sans", sans-serif; font-weight: 600; color: var(--white);
    font-size: 36px; line-height: 1; letter-spacing: .2px; white-space: nowrap;
  }
  .brand__rule { margin-top: 14px; width: 134px; height: 3px; background: var(--green); }
  .card--front .brand { right: 116px; top: 180px; }
  .card--back .brand { right: 32px; top: 90px; }

  .person { position: absolute; left: 31px; top: 197px; }
  .person__name { color: var(--blue); font-weight: 700; font-size: 21px; line-height: 1.1; }
  .person__title { color: var(--white); font-size: 16px; margin-top: 3px; }

  .contact { position: absolute; left: 333px; top: 188px; color: var(--white); font-size: 16px; line-height: 22px; }
  .contact__address { margin-bottom: 8px; }
  .contact__list { list-style: none; }
  .contact__item { display: flex; align-items: center; gap: 7px; height: 23px; }
  .contact__icon { width: 14px; height: 14px; fill: var(--green); flex: none; }

  .footer-band { position: absolute; left: 0; bottom: 0; width: 100%; }
  .footer-band__stripe { height: 4px; background: var(--blue); margin-bottom: 5px; }
  .footer-band__base { height: 42px; background: var(--green); }
</style>
</head>
<body>

<section class="card card--front" aria-label="Card front">
  <div class="brand">
    <div class="brand__row">
      <span class="brand__dot"></span>
      <span class="brand__name">Willowbend Pharmacy</span>
    </div>
    <span class="brand__rule"></span>
  </div>
</section>

<section class="card card--back" aria-label="Card back">
  <div class="brand">
    <div class="brand__row">
      <span class="brand__dot"></span>
      <span class="brand__name">Willowbend Pharmacy</span>
    </div>
    <span class="brand__rule"></span>
  </div>

  <div class="person">
    <p class="person__name">DORIAN KESSEL</p>
    <p class="person__title">Pharmacy Manager</p>
  </div>

  <div class="contact">
    <p class="contact__address">418 Fenwick Lane, Suite 12<br>Toronto Ontario M4K</p>
    <ul class="contact__list">
      <li class="contact__item">
        <svg class="contact__icon" viewBox="0 0 16 16"><path d="M3 2h3l1.5 3.5-2 1.2a8 8 0 0 0 3.8 3.8l1.2-2L14 10v3a1 1 0 0 1-1 1A11 11 0 0 1 2 3a1 1 0 0 1 1-1z"/></svg>
        555-014-2276 ext. 230
      </li>
      <li class="contact__item">
        <svg class="contact__icon" viewBox="0 0 16 16"><path d="M1 3h14v10H1z"/><path d="M1.5 3.5 8 9l6.5-5.5" fill="none" stroke="#232323" stroke-width="1.2"/></svg>
        Dorian@willowbendpharmacy.example
      </li>
      <li class="contact__item">
        <svg class="contact__icon" viewBox="0 0 16 16"><circle cx="8" cy="8" r="6.5" fill="none" stroke="#9cc63b" stroke-width="1.8"/><path d="M8 2v12M2 8h12" stroke="#9cc63b" stroke-width="1.4"/></svg>
        www.willowbendpharmacy.example
      </li>
    </ul>
  </div>

  <div class="footer-band" aria-hidden="true">
    <div class="footer-band__stripe"></div>
    <div class="footer-band__base"></div>
  </div>
</section>

</body>
</html>
```